Travel Company is looking for a STAND OUT Business Card

I need a unique Business Card that will truly stand out. Nothing too busy. Simple is good, right? Not looking for a standard design either. No cookie cutter layout. We are a Travel Company that works more with Companies than Travelers. I had an idea to focus and emphasis on the 2 logo a bit more. This is not necessary, however thought it would look interesting. I am just looking for something interesting and a bit different. Does't have to completely off the wall crazy, just not your run of the mill business card.

Target Market(s)

Hoteliers, Resort Management, Call Centers, Executives, Travelers, Families, Businesses

Industry/Entity Type

Hospitality

Contact Information for Business Card

President/CEO - Marcus T Bellamy (title not necessary if design doesn't allow for it)
contact - (407) 555-0186
email - mbellamy@wayfarenow.example
address - 4812 Quillmore Ave #164
Orlando, FL 32804
website - www.wayfarenow.example

Font styles to use
Serif
Other font styles liked:
• Avenir Next LT Pro BOLD

Requirements
Must have
• simple look and design. Unique design
Nice to have
• I attached the 2 logo separate from the main logo. This can be used separately from the Main Logo, together with the main logo or as main logo. I included the logo font. Use it or not, designers choice.
Should not have
• cookie cutter design. Little use of red other than the logo

```html
<!DOCTYPE html>
<html lang="en">
<head>
<meta charset="utf-8">
<title>wayfarenow business card</title>
<link rel="stylesheet" href="https://fonts.googleapis.com/css2?family=Figtree:wght@500;600;700&display=swap">
<style>
  :root {
    --backdrop: #d4d4d4;
    --brand-red: #ff0000;
    --paper: #ffffff;
    --ink: #000000;
    --card-w: 520px;
    --card-h: 289px;
  }
  * { box-sizing: border-box; margin: 0; padding: 0; }
  html, body {
    width: 1200px;
    height: 800px;
    overflow: hidden;
    background: var(--backdrop);
    font-family: "Figtree", "Helvetica Neue", Arial, sans-serif;
  }
  .stage {
    position: relative;
    width: 1200px;
    height: 800px;
  }
  .card {
    position: absolute;
    top: 255px;
    width: var(--card-w);
    height: var(--card-h);
    overflow: hidden;
  }

  /* Front */
  .card-front {
    left: 50px;
    background: var(--brand-red);
  }
  .front-block {
    position: absolute;
    left: 0;
    bottom: 0;
    width: 233px;
    height: 233px;
    background: var(--paper);
  }
  .front-wordmark {
    position: absolute;
    left: 312px;
    top: 123px;
    color: var(--paper);
    font-weight: 700;
    font-size: 27px;
    letter-spacing: 0.2px;
  }
  .front-url {
    position: absolute;
    right: 16px;
    bottom: 6px;
    color: var(--paper);
    font-weight: 700;
    font-size: 12px;
  }

  /* Back */
  .card-back {
    left: 630px;
    background: var(--paper);
  }
  .back-band {
    position: absolute;
    left: 0; top: 0;
    width: 100%;
    height: 27px;
    background: var(--brand-red);
  }
  .back-wordmark {
    position: absolute;
    left: 11px;
    top: 56px;
    color: var(--ink);
    font-weight: 700;
    font-size: 22px;
    letter-spacing: -0.3px;
  }
  .holder {
    position: absolute;
    right: 21px;
    top: 130px;
    text-align: left;
  }
  .holder-name {
    color: var(--brand-red);
    font-weight: 700;
    font-size: 20px;
    line-height: 1.05;
  }
  .holder-title {
    color: var(--ink);
    font-weight: 500;
    font-size: 14px;
    line-height: 1.1;
  }
  .contact-panel {
    position: absolute;
    left: 0;
    top: 182px;
    width: 100%;
    height: 107px;
    background: var(--ink);
    color: var(--paper);
    font-weight: 600;
    font-size: 12.5px;
  }
  .address {
    position: absolute;
    left: 23px;
    top: 8px;
    line-height: 15.5px;
  }
  .lines {
    position: absolute;
    left: 23px;
    top: 61px;
    line-height: 18px;
  }
  .label {
    color: var(--brand-red);
    font-weight: 700;
    display: inline-block;
    width: 19px;
  }
  .email {
    position: absolute;
    right: 13px;
    top: 79px;
    line-height: 18px;
  }
  .email .label { width: 18px; }
</style>
</head>
<body>
<main class="stage">
  <section class="card card-front" aria-label="Card front">
    <div class="front-block"></div>
    <p class="front-wordmark">wayfarenow</p>
    <p class="front-url">www.wayfarenow.example</p>
  </section>

  <section class="card card-back" aria-label="Card back">
    <div class="back-band"></div>
    <p class="back-wordmark">wayfarenow</p>
    <div class="holder">
      <p class="holder-name">Marcus T Bellamy</p>
      <p class="holder-title">President/CEO</p>
    </div>
    <div class="contact-panel">
      <p class="address">4812 Quillmore Ave #164<br>Orlando, FL 32804</p>
      <p class="lines">
        <span class="label">m</span>(407) 555-0186<br>
        <span class="label">w</span>www.wayfarenow.example
      </p>
      <p class="email"><span class="label">e</span>mbellamy@wayfarenow.example</p>
    </div>
  </section>
</main>
</body>
</html>
```